Business Card *

A business card design
Use the logo uploaded in the brief page.
You may use placeholders in your design layouts.
I will provide the actual business card details to the winning designer.

Logo
Place for contact info (name, title, phone, email, etc)

Requirements
Must have
• Logo

```html
<!DOCTYPE html>
<html lang="en">
<head>
<meta charset="utf-8">
<title>Kestrel Ridge Business Card</title>
<link rel="stylesheet" href="https://fonts.googleapis.com/css2?family=Archivo:wdth,wght@62..125,100..900&display=swap">
<style>
  :root {
    --backdrop: #c9c9c9;
    --card-white: #ffffff;
    --brand-green: #3bb54a;
    --brand-green-deep: #31a840;
    --brand-grey: #939598;
    --text-light: #ffffff;
    --text-mint: #d9f7dc;
  }
  * { margin: 0; padding: 0; box-sizing: border-box; }
  html, body {
    width: 1200px;
    height: 1000px;
    overflow: hidden;
    background: var(--backdrop);
    font-family: "Archivo", "Helvetica Neue", Arial, sans-serif;
    font-stretch: 125%;
  }
  .canvas { position: relative; width: 1200px; height: 1000px; }

  .card { position: absolute; width: 685px; height: 381px; overflow: hidden; }

  .card--front { left: 39px; top: 50px; background: var(--card-white); }
  .front-mark {
    position: absolute; left: 287px; top: 100px;
    width: 110px; height: 110px; border-radius: 50%;
    background: var(--brand-green);
  }
  .front-name {
    position: absolute; left: 0; right: 0; top: 232px;
    text-align: center;
    font-size: 36px; font-weight: 700; letter-spacing: 0.5px;
    color: var(--brand-grey);
  }

  .card--back { left: 474px; top: 463px; background: var(--brand-green); }
  .back-decoration {
    position: absolute; left: 350px; top: 36px;
    width: 310px; height: 310px; border-radius: 50%;
    background: var(--brand-green-deep);
  }
  .holder-name {
    position: absolute; left: 62px; top: 78px;
    font-size: 41px; font-weight: 700; line-height: 1;
    color: var(--text-light);
  }
  .holder-title {
    position: absolute; left: 64px; top: 121px;
    font-size: 15px; font-weight: 700; letter-spacing: 1px;
    color: var(--text-light);
  }
  .contact-list {
    position: absolute; left: 63px; top: 210px;
    list-style: none;
    font-size: 22px; font-weight: 700; line-height: 29px;
    color: var(--text-light);
  }
  .social {
    position: absolute; left: 64px; top: 295px;
    display: flex; align-items: center; gap: 10px;
    font-size: 19px; font-weight: 700;
    color: var(--text-mint);
  }
  .social-square { width: 26px; height: 26px; background: var(--text-light); }
</style>
</head>
<body>
<main class="canvas">
  <section class="card card--front" aria-label="Card front">
    <div class="front-mark"></div>
    <div class="front-name">KESTREL RIDGE</div>
  </section>

  <section class="card card--back" aria-label="Card back">
    <div class="back-decoration"></div>
    <div class="holder-name">NAME</div>
    <div class="holder-title">TITLE</div>
    <ul class="contact-list">
      <li>PHONE</li>
      <li>EMAIL</li>
    </ul>
    <div class="social">
      <span class="social-square"></span>
      <span>KESTREL RIDGE</span>
    </div>
  </section>
</main>
</body>
</html>
```